In Search of a FANTASTIC BUSINESS CARD REFRESH AND REDESIGN

I would like to redesign the current business card for my company.  There is a parent company, Brookfane Care Group, with 2 operating companies - Brookfane Homecare and Brookfane Senior Living.
I will include the current business card design, along with the 3 logos I would like incorporated.  The business card can be two sided.  I'm looking for something clean, professional, and a fresh new look.

Target Market(s)
Hospitals, social workers, insurance agents, family members of seniors
Industry/Entity Type
Healthcare
Contact Information for Business Card
Name, title of person, address, phone number, web address, email address
Look and feel
Each slider illustrates characteristics of the customer's brand and the style your logo design should communicate.

```html
<!DOCTYPE html>
<html lang="en">
<head>
<meta charset="utf-8">
<title>Brookfane Care Group – Business Card</title>
<link href="https://fonts.googleapis.com/css2?family=Arimo:wght@400;700&family=Open+Sans:ital@1&display=swap" rel="stylesheet">
<style>
  :root {
    --stage: #000000;
    --card: #ffffff;
    --ink: #111111;
    --homecare-pink: #f25fa6;
    --senior-green: #4dba92;
    --brand-black: #111111;
  }
  * { box-sizing: border-box; margin: 0; padding: 0; }
  html, body { width: 1200px; height: 1200px; overflow: hidden; background: var(--stage); }
  .stage { position: relative; width: 1200px; height: 1200px; background: var(--stage); }
  .card {
    position: absolute; left: 276px; width: 648px; height: 396px;
    background: var(--card); overflow: hidden; color: var(--ink);
    font-family: "Arimo", Arial, sans-serif;
  }
  .card--front { top: 171px; }
  .card--back { top: 634px; }

  .brand-row {
    position: absolute; top: 30px; left: 0; width: 100%;
    display: flex; justify-content: center; gap: 32px;
  }
  .brand {
    width: 120px; display: flex; flex-direction: column; align-items: center;
    text-align: center; font-weight: 700; font-size: 15px; line-height: 1.15;
  }
  .brand__mark { width: 34px; height: 34px; border-radius: 6px; margin-bottom: 10px; }
  .brand--homecare { color: var(--homecare-pink); }
  .brand--homecare .brand__mark { background: var(--homecare-pink); }
  .brand--group { color: var(--brand-black); }
  .brand--group .brand__mark { background: var(--brand-black); }
  .brand--senior { color: var(--senior-green); }
  .brand--senior .brand__mark { background: var(--senior-green); }

  .contact { position: absolute; left: 59px; top: 150px; }
  .contact__name { font-weight: 700; font-size: 27px; line-height: 1.1; }
  .contact__title { font-size: 19px; line-height: 1.2; margin-bottom: 8px; }
  .contact__line { font-size: 16.5px; line-height: 19.7px; }

  .web {
    position: absolute; top: 310px; left: 0; width: 100%; text-align: center;
    font-family: "Open Sans", Arial, sans-serif; font-style: italic; font-size: 16px;
  }
  .divider { position: absolute; top: 356px; height: 8px; }
  .divider--left { left: 0; width: 275px; background: linear-gradient(90deg, #000 0%, #000 50%, #fff 100%); }
  .divider--right { right: 0; width: 275px; background: linear-gradient(270deg, #000 0%, #000 50%, #fff 100%); }
  .divider__mark {
    position: absolute; top: 348px; left: 313px; width: 22px; height: 22px;
    border-radius: 4px; background: var(--brand-black);
  }

  .back-lockup {
    position: absolute; top: 96px; left: 0; width: 100%;
    display: flex; flex-direction: column; align-items: center;
  }
  .back-lockup__mark { width: 80px; height: 80px; border-radius: 12px; background: var(--brand-black); }
  .back-lockup__name {
    margin-top: 40px; font-weight: 700; font-size: 36px; line-height: 1.2; color: var(--brand-black);
  }
</style>
</head>
<body>
<main class="stage">
  <section class="card card--front">
    <div class="brand-row">
      <div class="brand brand--homecare"><span class="brand__mark"></span>Brookfane Homecare</div>
      <div class="brand brand--group"><span class="brand__mark"></span>Brookfane Care Group</div>
      <div class="brand brand--senior"><span class="brand__mark"></span>Brookfane Senior Living</div>
    </div>
    <div class="contact">
      <p class="contact__name">Marla Kealoha</p>
      <p class="contact__title">President, CEO</p>
      <p class="contact__line">480 Lanakila Ave., Suite 210, Honolulu, HI 96817</p>
      <p class="contact__line">Phone: (808) 555-0143</p>
      <p class="contact__line">Fax (808) 555-0178</p>
      <p class="contact__line">Marla@BrookfaneCare.com</p>
    </div>
    <p class="web">www.BrookfaneCare.com</p>
    <span class="divider divider--left"></span>
    <span class="divider divider--right"></span>
    <span class="divider__mark"></span>
  </section>

  <section class="card card--back">
    <div class="back-lockup">
      <span class="back-lockup__mark"></span>
      <p class="back-lockup__name">Brookfane Care Group</p>
    </div>
  </section>
</main>
</body>
</html>
```